I have a product im creating that I need an infographic/ecover for. The product is a Pdf/Excel worksheet and video instructions. Its Called The Amber Ledger Planner. a color im thinking of is having some kind of orange on this. I want a design that pops out and shows both a product box and workbook for the checklist itself and a dvd case for the video instructions. I've added my logo and a sample product box for you to take a look at. Remember though this is a Workbook/Checklist and also a video instructions. I DO NOT want you to just copy my logo design or even use the colors, just maybe a place for you to start. I have now added a picture of what a work book might look like. as well as some big dvd boxes

```html
<!DOCTYPE html>
<html lang="en">
<head>
<meta charset="utf-8">
<title>The Amber Ledger Planner – Cover</title>
<link rel="stylesheet" href="https://fonts.googleapis.com/css2?family=Anton&family=Playfair+Display:ital,wght@1,900&family=Oswald:wght@600;700&display=swap">
<style>
  :root {
    --page-bg: #e9e9e9;
    --amber-light: #ffd61f;
    --amber-mid: #fbb116;
    --amber-deep: #f38a1c;
    --ink-dark: #2b2b2b;
    --ink-blue: #1677b4;
    --art-tone: #fde38a;
  }
  * { margin: 0; padding: 0; box-sizing: border-box; }
  html, body {
    width: 1200px;
    height: 1111px;
    overflow: hidden;
    background: var(--page-bg);
  }
  .canvas {
    position: relative;
    width: 1200px;
    height: 1111px;
  }
  .cover {
    position: absolute;
    left: 330px;
    top: 30px;
    width: 540px;
    height: 1050px;
    background: radial-gradient(ellipse 70% 55% at 50% 45%, var(--amber-light) 0%, var(--amber-mid) 45%, var(--amber-deep) 100%);
    overflow: hidden;
  }
  .brand {
    position: absolute;
    top: 100px;
    left: 0;
    width: 100%;
    display: flex;
    flex-direction: column;
    align-items: center;
    gap: 6px;
  }
  .brand-dot {
    width: 44px;
    height: 44px;
    border-radius: 50%;
    background: var(--ink-dark);
  }
  .brand-name {
    font-family: "Oswald", sans-serif;
    font-weight: 600;
    font-size: 12px;
    letter-spacing: 1px;
    text-transform: uppercase;
    color: var(--ink-dark);
  }
  .title-lead {
    position: absolute;
    top: 196px;
    left: 160px;
    font-family: "Oswald", sans-serif;
    font-weight: 700;
    font-size: 44px;
    line-height: 1;
    color: var(--ink-dark);
  }
  .title-script {
    position: absolute;
    top: 250px;
    left: 0;
    width: 100%;
    text-align: center;
    font-family: "Playfair Display", serif;
    font-style: italic;
    font-weight: 900;
    font-size: 138px;
    line-height: 1;
    color: var(--ink-dark);
  }
  .desk-art {
    position: absolute;
    top: 430px;
    left: 50px;
    width: 440px;
    height: 240px;
    border-radius: 6px;
    background: radial-gradient(ellipse at center, #fff6cf 0%, var(--art-tone) 70%, rgba(253,227,138,0) 100%);
  }
  .title-block {
    position: absolute;
    left: 0;
    width: 100%;
    text-align: center;
    font-family: "Anton", sans-serif;
    line-height: 1;
    text-transform: uppercase;
  }
  .title-main {
    top: 690px;
    font-size: 170px;
    color: var(--ink-blue);
  }
  .title-sub {
    top: 885px;
    font-size: 132px;
    color: var(--ink-dark);
  }
</style>
</head>
<body>
  <div class="canvas">
    <section class="cover">
      <div class="brand">
        <span class="brand-dot"></span>
        <span class="brand-name">Quillmere Tallyworks</span>
      </div>
      <div class="title-lead">the</div>
      <h1 class="title-script">Amber</h1>
      <div class="desk-art" role="img" aria-label="Flat-lay illustration of a tablet, clipboard, pencils and a report with charts"></div>
      <div class="title-block title-main">Ledger</div>
      <div class="title-block title-sub">Planner</div>
    </section>
  </div>
</body>
</html>
```